Income Tax Business Cards - Updates

Need to update these business cards while keeping all the same wording but just update them and make them look nicer and more modern/ on brand with our brand.

Industry/Entity Type

finance

Contact Information for Business Card

we have multiple locations so will just need to easily be able to change the address and phone numbers

Colors

Designer to choose colors to be used in the design.

```html
<!DOCTYPE html>
<html lang="en">
<head>
<meta charset="utf-8">
<title>Ledgerline Financial Group – Tax Business Cards</title>
<link href="https://fonts.googleapis.com/css2?family=Montserrat:wght@600;700;900&family=Rubik:wght@400;500&display=swap" rel="stylesheet">
<style>
  :root {
    --brand-green: #1d6331;
    --brand-green-dark: #134a23;
    --brand-red: #c7313d;
    --brand-red-deep: #a82330;
    --card-white: #ffffff;
    --ink: #222222;
    --canvas: #eceae6;
  }
  * { box-sizing: border-box; margin: 0; padding: 0; }
  html, body { width: 1200px; height: 871px; overflow: hidden; }
  body {
    background: var(--canvas);
    font-family: "Montserrat", sans-serif;
    position: relative;
  }
  .card {
    position: absolute;
    width: 560px;
    height: 320px;
    background: var(--card-white);
    box-shadow: 0 8px 24px rgba(0,0,0,.12);
    overflow: hidden;
  }
  .card--front { left: 320px; top: 70px; }
  .card--back  { left: 320px; top: 470px; }

  /* brand name lockup */
  .brand {
    display: flex;
    align-items: center;
    gap: 8px;
    color: var(--brand-green);
    font-family: "Montserrat", sans-serif;
    font-weight: 700;
    letter-spacing: .5px;
  }
  .brand__mark { width: 14px; height: 14px; background: var(--brand-red); flex: none; }
  .brand__name { font-size: 22px; line-height: 1; }
  .brand--small .brand__name { font-size: 17px; }

  /* front */
  .front__brand { position: absolute; top: 44px; left: 0; right: 0; justify-content: center; }
  .front__headline {
    position: absolute; top: 92px; left: 0; right: 0;
    text-align: center;
    color: var(--brand-green);
    font-weight: 900;
    font-size: 40px;
    line-height: 1.05;
    text-transform: uppercase;
  }
  .front__offer {
    position: absolute; top: 196px; left: 0; right: 0;
    text-align: center;
    color: var(--brand-red);
    font-weight: 900;
    font-size: 19px;
    text-transform: uppercase;
  }
  .front__web {
    position: absolute; bottom: 30px; left: 0; right: 0;
    text-align: center;
    color: var(--brand-green);
    font-family: "Rubik", sans-serif;
    font-size: 15px;
  }
  .front__band {
    position: absolute; bottom: 0; left: 0; right: 0;
    height: 18px;
    background: var(--brand-green);
  }

  /* back */
  .back__banner { position: absolute; top: 0; left: 0; width: 560px; height: 150px; }
  .back__title {
    position: absolute; top: 18px; left: 0; right: 0;
    text-align: center;
    color: var(--card-white);
    font-weight: 900;
    font-size: 36px;
    line-height: 1.2;
    text-transform: uppercase;
    text-shadow: 2px 2px 0 var(--brand-red-deep);
  }
  .back__offer {
    position: absolute; top: 66px; left: 0; right: 0;
    text-align: center;
    color: var(--card-white);
    font-weight: 900;
    font-size: 15px;
    line-height: 1.25;
    text-transform: uppercase;
    text-shadow: -1.5px -1.5px 0 var(--brand-green), 1.5px -1.5px 0 var(--brand-green),
                 -1.5px 1.5px 0 var(--brand-green), 1.5px 1.5px 0 var(--brand-green);
  }
  .back__brand { position: absolute; right: 30px; bottom: 104px; }
  .contact { position: absolute; left: 26px; bottom: 18px; list-style: none; }
  .contact__row { display: flex; align-items: center; gap: 10px; margin-top: 6px; }
  .contact__row:first-child { margin-top: 0; }
  .contact__icon { width: 34px; height: 34px; flex: none; }
  .contact__lines {
    font-family: "Rubik", sans-serif;
    font-size: 10.5px;
    line-height: 1.25;
    color: var(--ink);
  }
</style>
</head>
<body>

  <section class="card card--front" aria-label="Business card front">
    <div class="brand front__brand">
      <span class="brand__mark"></span>
      <span class="brand__name">Ledgerline Financial Group</span>
    </div>
    <h1 class="front__headline">File your<br>taxes here</h1>
    <p class="front__offer">Upto $6,000 same day advance</p>
    <p class="front__web">www.ledgerline-tax.com</p>
    <div class="front__band"></div>
  </section>

  <section class="card card--back" aria-label="Business card back">
    <svg class="back__banner" viewBox="0 0 560 150" aria-hidden="true">
      <polygon points="0,0 560,0 560,114 300,114 250,148 0,148" fill="var(--brand-red)"/>
    </svg>
    <h2 class="back__title">Free estimates!</h2>
    <p class="back__offer">Upto $6,000 same day advance<br>on approved tax returns</p>

    <div class="brand brand--small back__brand">
      <span class="brand__mark"></span>
      <span class="brand__name">Ledgerline Financial Group</span>
    </div>

    <ul class="contact">
      <li class="contact__row">
        <svg class="contact__icon" viewBox="0 0 34 34" aria-hidden="true">
          <rect width="34" height="34" fill="var(--brand-red)"/>
          <rect x="11" y="6" width="12" height="22" rx="2" fill="none" stroke="#fff" stroke-width="2"/>
          <circle cx="17" cy="24" r="1.3" fill="#fff"/>
        </svg>
        <div class="contact__lines">555 . 014 2873<br>555 . 014 2874<br>555 . 014 2875</div>
      </li>
      <li class="contact__row">
        <svg class="contact__icon" viewBox="0 0 34 34" aria-hidden="true">
          <rect width="34" height="34" fill="var(--brand-green)"/>
          <rect x="7" y="10" width="20" height="14" fill="none" stroke="#fff" stroke-width="2"/>
          <polyline points="7,10 17,18 27,10" fill="none" stroke="#fff" stroke-width="2"/>
        </svg>
        <div class="contact__lines">office@ledgerline-tax.com<br>office@ledgerline-tax.com<br>office@ledgerline-tax.com</div>
      </li>
      <li class="contact__row">
        <svg class="contact__icon" viewBox="0 0 34 34" aria-hidden="true">
          <rect width="34" height="34" fill="var(--brand-red)"/>
          <path d="M17 27 C12 20 10 17 10 14 a7 7 0 0 1 14 0 c0 3 -2 6 -7 13z" fill="#fff"/>
          <circle cx="17" cy="14" r="2.6" fill="var(--brand-red)"/>
        </svg>
        <div class="contact__lines">4120 CEDAR RIDGE BLDG 3 #210 Austin, TX 78701<br>4120 CEDAR RIDGE BLDG 3 #210 Austin, TX 78701<br>4120 CEDAR RIDGE BLDG 3 #210 Austin, TX 78701</div>
      </li>
    </ul>
  </section>

</body>
</html>
```